Nightclub-type Event Poster Advertisement

Lumora Events is based in Christchurch, New Zealand and we have our next party coming up. We like a different flair for each of our events so are looking for some help from you guys. We are very flexible with everything - colours, layout, backgrounds, fonts, etc so it's ALL up to you. Attached is our company logo and the flyer (and poster) we used for our last party. Our website is lumoranz.example where you can find and use our photos and find more info about us if you desire.
Designs we are wanting: An A3 poster,an A6 flyer (smaller version of the poster is probably fine), tickets (140x68 mm). It would be great if a 5 mm bleed was included so we could get them printed directly.
Details for the event to be advertised are as followed:
Party Name: (TBD... will update ASAP)
05/07/2014
10pm-close
Lineup: 'Bazzo (Akl)', 'DJ Glimtrax', 'DJ's Morquent & Pelnavo', 'Quiet Harbour Pulse'.
Dorrin Hattles Central, Corner Fenwick & Oberly Streets
$10 Tickets
R18
Tickets & Enquiries: Marta on 0219047362
Presented by Lumora Entertainment
Thanks to everyone who reads this and please give it a go! Any questions don't hesitate to ask.
Target Market(s)
New Zealand Europeans in Christchurch, New Zealand between 18 and 25 years old.
Industry/Entity Type
Events
Look and feel

```html
<!DOCTYPE html>
<html lang="en">
<head>
<meta charset="utf-8">
<title>The Lumora – Event Poster</title>
<link rel="stylesheet" href="https://fonts.googleapis.com/css2?family=Comfortaa:wght@400;600&family=Open+Sans:wght@400;700&display=swap">
<style>
  :root {
    --navy-deep: #0a1250;
    --navy: #10248a;
    --blue-glow: #2f7fe0;
    --cyan-core: #8fe0ff;
    --title-cyan: #5fe6ff;
    --white: #ffffff;
    --rule: rgba(255, 255, 255, 0.55);
  }
  * { margin: 0; padding: 0; box-sizing: border-box; }
  html, body { width: 870px; height: 1200px; overflow: hidden; background: var(--navy-deep); }
  .poster {
    position: relative;
    width: 870px;
    height: 1200px;
    overflow: hidden;
    color: var(--white);
    font-family: "Open Sans", Arial, sans-serif;
    text-align: center;
    background:
      radial-gradient(ellipse 340px 300px at 436px 600px, var(--cyan-core) 0%, rgba(95, 190, 255, 0.6) 25%, rgba(47, 127, 224, 0) 70%),
      radial-gradient(ellipse 620px 720px at 436px 560px, var(--blue-glow) 0%, var(--navy) 55%, var(--navy-deep) 100%);
  }
  .poster > * { position: absolute; left: 0; width: 100%; }
  .presenter-label { top: 45px; font-size: 21px; }
  .presenter-name { top: 72px; font-size: 21px; font-weight: 700; }
  .title-article {
    top: 150px; font-family: "Comfortaa", sans-serif; font-size: 72px; font-weight: 400;
  }
  .title-main {
    top: 238px; font-family: "Comfortaa", sans-serif; font-size: 84px; font-weight: 600;
    letter-spacing: 3px; color: var(--title-cyan);
    text-shadow: 0 0 14px rgba(95, 230, 255, 0.8);
  }
  .event-date { top: 338px; font-size: 35px; font-weight: 400; letter-spacing: 1px; }
  .hero-art {
    top: 435px; left: 150px; width: 590px; height: 375px; border-radius: 40%;
    background: radial-gradient(ellipse at center, rgba(255, 255, 255, 0.35) 0%, rgba(20, 30, 60, 0.55) 55%, rgba(20, 30, 60, 0) 75%);
  }
  .rule { height: 1px; background: var(--rule); }
  .rule-top { top: 831px; left: 125px; width: 610px; }
  .rule-bottom { top: 914px; left: 86px; width: 697px; }
  .lineup { top: 840px; font-size: 19px; font-weight: 700; letter-spacing: 2px; line-height: 34px; }
  .venue { top: 928px; font-size: 18px; font-weight: 700; letter-spacing: 1px; }
  .details { top: 966px; font-size: 31px; line-height: 51px; }
  .organiser-mark {
    top: 1132px; left: 120px; width: auto; display: flex; align-items: center; gap: 8px;
    font-size: 16px;
  }
  .organiser-mark .dot { width: 10px; height: 10px; border: 1px solid var(--white); }
  .enquiries { top: 1136px; left: 255px; width: auto; font-size: 16px; text-align: left; }
</style>
</head>
<body>
  <main class="poster">
    <p class="presenter-label">Presented by</p>
    <p class="presenter-name">Lumora Entertainment</p>
    <h1 class="title-article">The</h1>
    <h2 class="title-main">LUMORA</h2>
    <p class="event-date">05/07/2014</p>
    <div class="hero-art" role="img" aria-label="Silhouettes of a guitarist and a dancer with raised arms over speaker circles and swirling ornaments"></div>
    <div class="rule rule-top"></div>
    <p class="lineup">BAZZO (AKL), DJ GLIMTRAX, DJ'S MORQUENT &amp; PELNAVO,<br>QUIET HARBOUR PULSE</p>
    <div class="rule rule-bottom"></div>
    <p class="venue">Dorrin Hattles Central, Corner Fenwick &amp; Oberly Streets</p>
    <p class="details">R18<br>$10 Tickets<br>10pm-close</p>
    <div class="organiser-mark"><span class="dot"></span><span>Lumora</span></div>
    <p class="enquiries">Tickets &amp; Enquiries: Marta on 0219047362</p>
  </main>
</body>
</html>
```